Lumokrest Mobile App

I need a professional, sleek design for a new mobile application for Zentab. The application will be the mobile counterpart to the current website (www.lumokrest-app.net - please refer to site for existing web design).
Lumokrest is a photo social network which focuses on content aggregation, search and real-time photo discovery.
I need a clean, modern, minimalistic design for the mobile app which will run on Zentab, including minimalistic page and button designs.
I've attached undesigned screenshots of the current application build to give an idea of the functionality and pages available within the application.
The app will have the following pages/functionality:
- photo feed of other users' images; data presented: photo, photo caption, user name, date
- upload photo
- save photo
- photo search; available search criteria: keywords, dates (from/to), location
Photographers/Photo enthusiasts, bloggers, social networking
Build

```html
<!DOCTYPE html>
<html lang="en">
<head>
<meta charset="utf-8">
<title>Lumokrest – Search</title>
<link rel="stylesheet" href="https://fonts.googleapis.com/css2?family=Ubuntu:wght@400;500;700&display=swap">
<style>
  :root {
    --header-bg: #161718;
    --header-edge: #2a2c30;
    --body-top: #2c2f34;
    --body-mid: #3a3d44;
    --tabbar-bg: #1a1b1c;
    --field-bg: #151618;
    --field-edge: #0b0c0d;
    --text: #ffffff;
    --label: #e8e8e8;
    --green-light: #a3cc45;
    --green: #86b52c;
    --green-dark: #5f8a17;
    --icon-white: #f2f2f2;
  }
  html, body {
    margin: 0;
    width: 676px;
    height: 1200px;
    overflow: hidden;
    background: var(--tabbar-bg);
  }
  .screen {
    position: relative;
    width: 640px;
    height: 1136px;
    transform: scale(1.05625);
    transform-origin: 0 0;
    font-family: "Ubuntu", sans-serif;
    color: var(--text);
    background:
      radial-gradient(ellipse 70% 55% at 55% 50%, var(--body-mid), transparent 80%),
      linear-gradient(180deg, var(--body-top), #353840 50%, #2f3237);
    overflow: hidden;
  }
  .app-header {
    position: absolute; inset: 0 0 auto 0;
    height: 88px;
    background: var(--header-bg);
    border-bottom: 2px solid var(--header-edge);
  }
  .back-button {
    position: absolute; left: 26px; top: 27px;
    width: 144px; height: 36px;
  }
  .back-button svg { position: absolute; inset: 0; }
  .back-button span {
    position: absolute; left: 50px; top: 8px;
    font-size: 18px; font-weight: 500; color: var(--text);
  }
  .screen-title {
    position: absolute; left: 0; right: 0; top: 26px;
    margin: 0; text-align: center;
    font-size: 30px; font-weight: 700; letter-spacing: 0.5px;
    padding-left: 28px;
  }
  .search-form { position: absolute; left: 0; top: 0; }
  .form-label {
    position: absolute; right: 509px; width: 120px;
    text-align: right; font-size: 17px; color: var(--label);
  }
  .field {
    position: absolute; box-sizing: border-box;
    background: var(--field-bg);
    border: 1px solid var(--field-edge);
    border-radius: 17px;
    box-shadow: inset 0 2px 3px rgba(0,0,0,.6), 0 1px 0 rgba(255,255,255,.07);
    font-size: 17px; color: var(--text);
    padding-left: 20px; line-height: 32px;
  }
  .field.is-focused {
    border: 3px solid var(--green);
    border-radius: 20px;
    line-height: 34px; padding-left: 21px;
  }
  .range-to { position: absolute; left: 295px; top: 215px; font-size: 17px; color: var(--label); }
  .search-button {
    position: absolute; left: 149px; top: 254px;
    width: 136px; height: 35px; border-radius: 18px;
    background: linear-gradient(180deg, var(--green-light), var(--green) 55%, var(--green-dark));
    box-shadow: 0 1px 2px rgba(0,0,0,.6);
    text-align: center; line-height: 35px;
    font-size: 17px; color: var(--text);
  }
  .tab-bar {
    position: absolute; left: 0; right: 0; bottom: 0;
    height: 91px; background: var(--tabbar-bg);
    border-top: 1px solid #0c0c0d;
  }
  .tab-indicator { position: absolute; left: 233px; top: -8px; }
  .tab-icon { position: absolute; }
</style>
</head>
<body>
<div class="screen">
  <header class="app-header">
    <div class="back-button">
      <svg width="144" height="36" viewBox="0 0 144 36">
        <defs>
          <linearGradient id="backFill" x1="0" y1="0" x2="0" y2="1">
            <stop offset="0" stop-color="#a3cc45"/>
            <stop offset=".55" stop-color="#86b52c"/>
            <stop offset="1" stop-color="#5f8a17"/>
          </linearGradient>
        </defs>
        <path d="M18 0 H144 V36 H18 L0 18 Z" fill="url(#backFill)"/>
        <path d="M25 11 L18 18 L25 25" fill="none" stroke="#1f2a0a" stroke-width="3.5" stroke-linecap="round" stroke-linejoin="round"/>
      </svg>
      <span>Back</span>
    </div>
    <h1 class="screen-title">SEARCH</h1>
  </header>

  <form class="search-form">
    <label class="form-label" style="top:123px">Search</label>
    <div class="field" style="left:149px;top:116px;width:436px;height:34px">Search Text</div>

    <label class="form-label" style="top:168px">Location</label>
    <div class="field is-focused" style="left:147px;top:158px;width:440px;height:40px">New Yo</div>

    <label class="form-label" style="top:215px">Date</label>
    <div class="field" style="left:149px;top:208px;width:136px;height:34px">02-02-2012</div>
    <span class="range-to">to</span>
    <div class="field" style="left:321px;top:208px;width:136px;height:34px">02-02-2012</div>

    <div class="search-button">Search</div>
  </form>

  <nav class="tab-bar">
    <svg class="tab-indicator" width="12" height="8" viewBox="0 0 12 8"><path d="M0 8 L6 0 L12 8 Z" fill="#1a1b1c"/></svg>

    <svg class="tab-icon" style="left:68px;top:23px" width="68" height="48" viewBox="0 0 68 48" aria-label="Shuffle feed">
      <g fill="none" stroke="var(--icon-white)" stroke-width="7">
        <path d="M0 13 H14 C26 13 30 35 42 35 H54"/>
        <path d="M0 35 H14 C20 35 23 30 26 25"/>
        <path d="M32 18 C35 15 38 13 42 13 H54"/>
      </g>
      <path d="M52 2 L66 13 L52 24 Z M52 24 L66 35 L52 46 Z" fill="var(--icon-white)"/>
    </svg>

    <svg class="tab-icon" style="left:208px;top:16px" width="62" height="60" viewBox="0 0 62 60" aria-label="Search">
      <g fill="#8cc63f">
        <path d="M31 0 L62 16 V21 H0 V16 Z"/>
        <rect x="5" y="24" width="52" height="4"/>
        <rect x="9" y="30" width="9" height="20"/>
        <rect x="26.5" y="30" width="9" height="20"/>
        <rect x="44" y="30" width="9" height="20"/>
        <rect x="5" y="52" width="52" height="3"/>
        <rect x="1" y="57" width="60" height="3"/>
      </g>
      <circle cx="31" cy="12" r="3.5" fill="#1a1b1c"/>
    </svg>

    <svg class="tab-icon" style="left:350px;top:17px" width="72" height="58" viewBox="0 0 72 58" aria-label="Upload photo">
      <path d="M22 6 Q22 2 26 2 H46 Q50 2 50 6 V9 H66 Q70 9 70 13 V54 Q70 57 66 57 H6 Q2 57 2 54 V13 Q2 9 6 9 H22 Z" fill="var(--icon-white)"/>
      <circle cx="36" cy="34" r="16" fill="#1a1b1c"/>
      <path d="M36 23 L46 34 H40 V44 H32 V34 H26 Z" fill="var(--icon-white)"/>
    </svg>

    <svg class="tab-icon" style="left:498px;top:25px" width="68" height="46" viewBox="0 0 68 46" aria-label="Profile">
      <rect x="0" y="0" width="68" height="40" rx="3" fill="var(--icon-white)"/>
      <rect x="10" y="38" width="6" height="8" fill="var(--icon-white)"/>
      <rect x="52" y="38" width="6" height="8" fill="var(--icon-white)"/>
      <g fill="#1a1b1c">
        <circle cx="19" cy="14" r="6"/>
        <path d="M8 32 Q8 22 19 22 Q30 22 30 32 Z"/>
        <rect x="36" y="8" width="24" height="3"/>
        <rect x="36" y="15" width="24" height="3"/>
        <rect x="36" y="22" width="24" height="3"/>
        <rect x="36" y="29" width="24" height="3"/>
      </g>
    </svg>
  </nav>
</div>
</body>
</html>
```